New business card for UK roofing company

We are Brindmore Roofing and we need a business card design for our staff.

We offer the following services:

- New roofs
- General roof repairs
- Drone surveys
- Single ply roofing
- Steel cladding
- Asbestos removal
- Electronic leak detection

I have attached our logo. I have also attached example branding printed to our vans. The business card should fit in with the style of our branding.

The business card should have the following information;

Address:
Unit 17c Wendlecroft Farm
Wendlecroft Lane
Hatchington
CM4 9QD

Telephone: 020 7946 0372
24 Hour: 0800 612 4479

Email: ray@brindmoreroofing.example
Mobile: 07700981234
Name: Ray Tunstead
Website: www.brindmoreroofing.example

The business card will be printed in Spot UV, see here: https://www.kestaprint.example/business-cards/spot-uv/

If you need anymore info, please let me know,

```html
<!DOCTYPE html>
<html lang="en">
<head>
<meta charset="utf-8">
<title>Brindmore Roofing – Business Card</title>
<link href="https://fonts.googleapis.com/css2?family=Manrope:wght@500;600;700;800&display=swap" rel="stylesheet">
<style>
  :root {
    --navy: #0b4a7d;
    --cyan: #14afdd;
    --paper: #ffffff;
    --backdrop: #e5e5e5;
  }
  * { margin: 0; padding: 0; box-sizing: border-box; }
  html, body { width: 1200px; height: 1200px; overflow: hidden; }
  body {
    background: var(--backdrop);
    font-family: "Manrope", sans-serif;
    position: relative;
  }
  .card {
    position: absolute;
    left: 371px;
    width: 459px;
    height: 275px;
    background: var(--paper);
    overflow: hidden;
  }
  .card--front { top: 247px; }
  .card--back { top: 684px; }

  /* Front */
  .brand {
    position: absolute;
    left: 43px;
    top: 106px;
    display: flex;
    align-items: center;
    gap: 12px;
  }
  .brand__dot {
    width: 48px; height: 48px;
    border-radius: 50%;
    background: var(--navy);
    flex: none;
  }
  .brand__name {
    font-weight: 800;
    font-size: 34px;
    letter-spacing: -1px;
    color: var(--navy);
    line-height: 1;
  }
  .tagline {
    position: absolute;
    left: 0; right: 0;
    top: 158px;
    text-align: center;
    font-weight: 700;
    font-size: 21px;
    letter-spacing: -0.6px;
    color: var(--navy);
  }
  .phones {
    position: absolute;
    left: 0; right: 0;
    top: 233px;
    text-align: center;
    font-weight: 600;
    font-size: 14.5px;
    line-height: 14.5px;
    letter-spacing: 0.3px;
    color: var(--navy);
  }
  .phones .label { color: var(--cyan); font-weight: 500; }

  /* Back */
  .decor-band {
    position: absolute;
    left: 0; right: 0; bottom: 0;
    height: 62px;
    background: linear-gradient(90deg, var(--cyan) 0%, var(--navy) 70%);
  }
  .person {
    position: absolute;
    left: 41px;
    top: 36px;
    font-weight: 800;
    font-size: 41px;
    letter-spacing: -1.6px;
    color: var(--navy);
  }
  .contact {
    position: absolute;
    left: 40px;
    top: 97px;
    list-style: none;
    color: var(--navy);
    font-weight: 700;
    font-size: 18.5px;
    line-height: 24px;
  }
  .contact li { display: flex; align-items: center; gap: 10px; }
  .contact svg { width: 15px; height: 15px; flex: none; }
  .address {
    position: absolute;
    left: 39px;
    top: 166px;
    font-style: normal;
    font-weight: 500;
    font-size: 9.5px;
    line-height: 14.5px;
    color: var(--navy);
  }
  .back-brand {
    position: absolute;
    right: 22px;
    top: 224px;
    text-align: center;
    color: var(--paper);
  }
  .back-brand__name {
    font-weight: 800;
    font-size: 19px;
    letter-spacing: -0.6px;
    line-height: 1;
  }
  .back-brand__url {
    font-weight: 500;
    font-size: 9.5px;
    margin-top: 3px;
  }
</style>
</head>
<body>

<section class="card card--front">
  <div class="brand">
    <span class="brand__dot"></span>
    <span class="brand__name">Brindmore Roofing</span>
  </div>
  <p class="tagline">Your local roofing experts</p>
  <p class="phones">
    <span class="label">Telephone:</span> 020 7946 0372<br>
    <span class="label">24 Hour:</span> 0800 612 4479
  </p>
</section>

<section class="card card--back">
  <div class="decor-band" role="img" aria-label="Cyan and navy wave decoration"></div>

  <h1 class="person">Ray Tunstead</h1>
  <ul class="contact">
    <li>
      <svg viewBox="0 0 16 16"><path fill="var(--cyan)" d="M12.5 1.5l1.8 1.8-2 2.6-1.4-.6c-.9 1.9-2.3 3.6-4 4.9l.5 1.4-2.6 2-1.8-1.8C5 9.5 8.5 5.2 12.5 1.5z"/></svg>
      ray@brindmoreroofing.example
    </li>
    <li>
      <svg viewBox="0 0 16 16"><rect x="1.5" y="3.5" width="13" height="9" fill="none" stroke="var(--cyan)" stroke-width="1.3"/><path d="M1.5 3.5l6.5 5 6.5-5" fill="none" stroke="var(--cyan)" stroke-width="1.3"/></svg>
      07700981234
    </li>
  </ul>
  <address class="address">
    Unit 17c Wendlecroft Farm<br>
    Wendlecroft Lane<br>
    Hatchington, CM4 9QD
  </address>

  <div class="back-brand">
    <div class="back-brand__name">Brindmore Roofing</div>
    <div class="back-brand__url">www.brindmoreroofing.example</div>
  </div>
</section>

</body>
</html>
```